Cultural Values, and Purpose, Vision and Mission statements design

We have recently created Cultural Values, and Purpose, Vision and Mission statements for a client’s business. We would like a visual representation created of each of these, to be hung on display in their office. For this project, we would like four (4) graphic design prints drawn up that depict:1. Purpose2. Vision3. Mission4. Cultural ValuesAll print designs should use a recurring, common theme, and be reflective of the business’ colours (see attached logo.)Please read and follow specifications in attached design brief.
Updates

Need extra days to review

Target Market(s)

Females, aged between 37 and 57 years old, who are family orientated, living locally, married and have between 1 and 3 children living at home.

Requirements
Must have
• Photoshop (PSD) format: All completed design will need to be in Photoshop (PSD) format before being handed over. This is to ensure that we can make alterations before printing if necessary.
• Quality: All designs must be 300 pixels resolution or higher.
• Purpose, Vision & Mission Designs Dimensions: The dimensions for each of the Purpose, Vision and Mission designs will need to be 30.5cm x 40.6cm (portrait, rectangle shape) with a surrounding 3.8cm border as it will be printed onto canvas matching these specifications.
• Cultural Values Dimensions: There are no specific dimensions required for the Cultural Values so the designer should feel free to display them best they see fit.
• Theme: All must follow the same theme and be reflective of the business's colours and logo.

```html
<!DOCTYPE html>
<html lang="en">
<head>
<meta charset="utf-8">
<title>Purpose – Ridgeway Motors</title>
<link rel="stylesheet" href="https://fonts.googleapis.com/css2?family=Montserrat:wght@900&family=Ubuntu:wght@400;500&display=swap">
<style>
  :root {
    --brand-orange: #f58220;
    --brand-grey: #8a8a8c;
    --paper: #ffffff;
    --ink: #111111;
    --watermark: #e3e3e3;
  }
  * { margin: 0; padding: 0; box-sizing: border-box; }
  html, body { width: 902px; height: 1200px; overflow: hidden; background: var(--paper); }
  .poster {
    position: relative;
    width: 902px;
    height: 1200px;
    overflow: hidden;
    background: var(--paper);
    font-family: "Ubuntu", sans-serif;
  }
  .brand {
    position: absolute;
    top: 84px;
    left: 0;
    width: 100%;
    display: flex;
    flex-direction: column;
    align-items: center;
  }
  .brand-name {
    display: flex;
    align-items: center;
    gap: 10px;
    font-weight: 500;
    font-size: 30px;
    line-height: 1;
    color: var(--brand-orange);
  }
  .brand-mark {
    width: 26px;
    height: 26px;
    background: var(--brand-orange);
  }
  .brand-tagline {
    margin-top: 8px;
    font-size: 10px;
    letter-spacing: 2.4px;
    color: var(--brand-grey);
  }
  .statement-band {
    position: absolute;
    top: 166px;
    left: 0;
    width: 100%;
    height: 344px;
    background: var(--brand-orange);
    color: var(--paper);
    text-align: center;
  }
  .statement-title {
    margin-top: 60px;
    font-family: "Montserrat", sans-serif;
    font-weight: 900;
    font-size: 138px;
    line-height: 1;
    letter-spacing: -1px;
  }
  .statement-text {
    margin: 8px auto 0;
    width: 700px;
    font-size: 28px;
    line-height: 28px;
  }
  .target-decoration {
    position: absolute;
    left: 324px;
    top: 607px;
    width: 696px;
    height: 696px;
    border-radius: 50%;
    background: radial-gradient(circle, var(--watermark) 0%, #eeeeee 60%, var(--watermark) 100%);
    opacity: 0.8;
  }
  .footnote {
    position: absolute;
    left: 56px;
    top: 1094px;
    font-size: 20px;
    line-height: 27px;
    color: var(--ink);
  }
</style>
</head>
<body>
  <main class="poster">
    <header class="brand">
      <div class="brand-name"><span class="brand-mark"></span>Ridgeway Motors</div>
      <div class="brand-tagline">DRIVING YOUR FAMILY HOME</div>
    </header>

    <section class="statement-band">
      <h1 class="statement-title">PURPOSE</h1>
      <p class="statement-text">Providing vehicle safety and security to Gippsland families on our country roads.</p>
    </section>

    <div class="target-decoration" role="img" aria-label="Large faint grey target with arrow decoration"></div>

    <p class="footnote">Lorem ipsum<br>dolor sit anem</p>
  </main>
</body>
</html>
```